LRW Automotive needs a catchy banner design

We need a design for a banner to be displayed on the fence in the outfield of a baseball stadium to show off our company and have people interested in what we do. We need something catchy that's going to attract people to look over at our banner.
We are a
Complete Automotive Service Company
Tires - Service - Repair - Diesel
We are in a Town called Cedar-Hollow
(555)214-3086 we would like the phone number to be a descent size so when you are in the stands you can read it.
I have attached what we came up with but like I said we need it to pop more and make the viewer that's looking at it want to look us up.
The Banner size is 24ft long and 10ft tall

```html
<!DOCTYPE html>
<html lang="en">
<head>
<meta charset="utf-8">
<title>LRW Service Company – Outfield Banners</title>
<link href="https://fonts.googleapis.com/css2?family=Orbitron:wght@500;700&family=Roboto:wght@400;700&display=swap" rel="stylesheet">
<style>
  :root{
    --canvas:#bdbec0;
    --blue:#1565d8;
    --blue-bright:#1e6ff0;
    --blue-deep:#0b4aa8;
    --panel-blue:#0d62b4;
    --wedge-blue:#0a4d8f;
    --ink:#0a0a0a;
    --yellow:#f7c31c;
    --white:#ffffff;
    --label-blue:#1a6fd1;
  }
  *{margin:0;padding:0;box-sizing:border-box}
  html,body{width:1200px;height:1150px;overflow:hidden;background:var(--canvas)}
  .canvas{position:relative;width:1200px;height:1150px}
  .banner{position:absolute;left:81px;width:1037px;height:431px;overflow:hidden}
  .banner--blue{top:103px}
  .banner--split{top:614px;background:var(--white)}
  .banner svg.shapes{position:absolute;inset:0}
  .txt{position:absolute;white-space:nowrap}
  .display{font-family:"Orbitron",sans-serif;font-weight:700;color:var(--white);font-size:34px;line-height:38px;letter-spacing:0}
  .label{font-family:"Orbitron",sans-serif;font-weight:500;font-size:15px;color:var(--yellow)}
  .value{font-family:"Orbitron",sans-serif;font-weight:500;font-size:14px;color:var(--white);letter-spacing:.5px}
  .services-line{font-family:"Orbitron",sans-serif;font-weight:500;font-size:13px;color:var(--white);letter-spacing:.5px;word-spacing:3px}
  .brand-mark{font-family:"Orbitron",sans-serif;font-weight:700;font-size:34px;color:var(--blue-deep);letter-spacing:2px}
  .label--blue{font-family:"Roboto",sans-serif;font-weight:400;font-size:15px;color:var(--label-blue)}
  .value--bold{font-family:"Roboto",sans-serif;font-weight:700;font-size:15px;color:var(--white)}
  .service-name{font-family:"Roboto",sans-serif;font-weight:700;font-size:24px;color:var(--white)}
</style>
</head>
<body>
<main class="canvas">

  <!-- Banner one: blue -->
  <section class="banner banner--blue">
    <svg class="shapes" width="1037" height="431" viewBox="0 0 1037 431">
      <defs>
        <linearGradient id="blueBg" x1="0" y1="0" x2="1" y2="1">
          <stop offset="0" stop-color="#1a5fd0"/>
          <stop offset=".5" stop-color="#1552c4"/>
          <stop offset="1" stop-color="#1f74ee"/>
        </linearGradient>
        <linearGradient id="tireTone" x1="0" y1="0" x2="0" y2="1">
          <stop offset="0" stop-color="#3a3a3a"/>
          <stop offset="1" stop-color="#141414"/>
        </linearGradient>
      </defs>
      <rect width="1037" height="431" fill="url(#blueBg)" role="img" aria-label="Background photo of a mechanic carrying a tire, tinted blue"/>
      <rect x="-182" y="-182" width="363" height="363" rx="70" transform="translate(788 246) rotate(45)" fill="none" stroke="var(--white)" stroke-width="1.5"/>
      <rect x="-164" y="-164" width="328" height="328" rx="62" transform="translate(760 246) rotate(45)" fill="var(--white)"/>
      <rect x="-82" y="-82" width="164" height="164" rx="34" transform="translate(563 35) rotate(45)" fill="var(--white)"/>
      <rect x="604" y="127" width="312" height="239" rx="40" fill="url(#tireTone)" role="img" aria-label="Photo of a stack of car tires"/>
      <!-- contact icons -->
      <rect x="-20" y="-20" width="40" height="40" rx="8" transform="translate(107 187) rotate(45)" fill="var(--yellow)"/>
      <path d="M107 176a7 7 0 0 1 7 7c0 5-7 12-7 12s-7-7-7-12a7 7 0 0 1 7-7z" fill="var(--blue-deep)"/>
      <circle cx="107" cy="183" r="2.5" fill="var(--yellow)"/>
      <rect x="-20" y="-20" width="40" height="40" rx="8" transform="translate(107 259) rotate(45)" fill="var(--yellow)"/>
      <path d="M100 251c2-2 4-2 5 0l2 3c1 1 0 2-1 3l-1 1c1 2 3 4 5 5l1-1c1-1 2-2 3-1l3 2c2 1 2 3 0 5-3 3-8 1-13-4s-7-10-4-13z" fill="var(--blue-deep)"/>
    </svg>
    <div class="txt brand-mark" style="left:563px;top:48px;transform:translateX(-50%)">LRW</div>
    <div class="txt display" style="left:72px;top:62px">LRW SERVICE<br>COMPANY</div>
    <div class="txt label" style="left:150px;top:165px">Location :</div>
    <div class="txt value" style="left:150px;top:191px">CEDAR-HOLLOW</div>
    <div class="txt label" style="left:150px;top:237px">Phone :</div>
    <div class="txt value" style="left:150px;top:262px">(555)214-3086</div>
    <div class="txt services-line" style="left:81px;top:362px">TIRES &nbsp;| &nbsp;SERVICE &nbsp;| &nbsp;REPAIR &nbsp;| &nbsp;DIESEL</div>
  </section>

  <!-- Banner two: white, black and blue -->
  <section class="banner banner--split">
    <svg class="shapes" width="1037" height="431" viewBox="0 0 1037 431">
      <polygon points="794,0 600,262 751,271 727,431 1037,431 1037,0" fill="var(--wedge-blue)"/>
      <polygon points="794,0 1037,0 1037,431 727,431 751,271" fill="var(--panel-blue)"/>
      <polygon points="0,212 751,266 751,271 745,431 0,431" fill="var(--blue)"/>
      <polygon points="0,218 749,273 727,431 0,431" fill="var(--ink)" role="img" aria-label="Dark photo of a tire in a workshop"/>
      <rect x="47" y="43" width="511" height="233" rx="60" fill="#2b2b2b" role="img" aria-label="Photo of a black SUV"/>
      <!-- contact icons -->
      <rect x="-20" y="-20" width="40" height="40" rx="8" transform="translate(518 312) rotate(45)" fill="var(--label-blue)"/>
      <path d="M518 301a7 7 0 0 1 7 7c0 5-7 12-7 12s-7-7-7-12a7 7 0 0 1 7-7z" fill="var(--white)"/>
      <circle cx="518" cy="308" r="2.5" fill="var(--label-blue)"/>
      <rect x="-20" y="-20" width="40" height="40" rx="8" transform="translate(518 383) rotate(45)" fill="var(--label-blue)"/>
      <path d="M511 375c2-2 4-2 5 0l2 3c1 1 0 2-1 3l-1 1c1 2 3 4 5 5l1-1c1-1 2-2 3-1l3 2c2 1 2 3 0 5-3 3-8 1-13-4s-7-10-4-13z" fill="var(--white)"/>
      <!-- service hexagons -->
      <g fill="var(--white)">
        <polygon points="869,33 897,49 897,81 869,97 841,81 841,49"/>
        <polygon points="857,127 885,143 885,175 857,191 829,175 829,143"/>
        <polygon points="845,222 873,238 873,270 845,286 817,270 817,238"/>
        <polygon points="833,316 861,332 861,364 833,380 805,364 805,332"/>
      </g>
      <g fill="none" stroke="var(--panel-blue)" stroke-width="3">
        <circle cx="869" cy="65" r="17"/><circle cx="869" cy="65" r="11"/>
        <path d="M869 54v22M858 65h22M861 57l16 16M877 57l-16 16" stroke-width="2"/>
        <path d="M843 166c6-4 10 2 18 0l8-4" stroke-linecap="round"/>
        <path d="M834 275l22-22M836 244l20 20" stroke-linecap="round"/>
        <rect x="821" y="338" width="20" height="24" rx="3"/>
        <path d="M841 342l6-6"/>
      </g>
      <g fill="var(--panel-blue)">
        <circle cx="857" cy="149" r="5"/><path d="M849 161a8 6 0 0 1 16 0z"/>
        <circle cx="856" cy="264" r="5"/>
      </g>
    </svg>
    <div class="txt brand-mark" style="left:625px;top:45px;transform:translateX(-50%)">LRW</div>
    <div class="txt display" style="left:52px;top:305px;line-height:44px">LRW SERVICE<br>COMPANY</div>
    <div class="txt label--blue" style="left:560px;top:288px">Location :</div>
    <div class="txt value--bold" style="left:560px;top:313px">CEDAR-HOLLOW</div>
    <div class="txt label--blue" style="left:560px;top:360px">Phone :</div>
    <div class="txt value--bold" style="left:560px;top:385px">(555)214-3086</div>
    <div class="txt service-name" style="left:919px;top:49px">TIRES</div>
    <div class="txt service-name" style="left:907px;top:144px">SERVICE</div>
    <div class="txt service-name" style="left:895px;top:239px">REPAIR</div>
    <div class="txt service-name" style="left:883px;top:332px">DIESEL</div>
  </section>

</main>
</body>
</html>
```